Website Design for BRAVO FREIGHTWAY

Hello. We are a Freight Brokage business in the transportation and logistics industry in the USA. Company name is BRAVO FREIGHTWAY. I'm looking to have a 5 page or less website built. Must have HOME, SHIPPERS, CARRIERS, ABOUT and CONTACT US.. I have additional information that needs to be placed in the footer of the website. Company address, contact info privacy and terms and conditions Need nice, vibrant looking site. The website needs to be a fully functionable site that is built and coded for wordpress and ready for hosting. Please visit these link for you to have an idea of the look and feel I want. www.tolvanhaulage.example www.corvel-transit.example. Will have logo concept in 2 days for upload. As time goes by I will supply more content and the layout of the respective pages.

```html
<!DOCTYPE html>
<html lang="en">
<head>
<meta charset="utf-8">
<title>Bravo Freightway</title>
<link rel="stylesheet" href="https://fonts.googleapis.com/css2?family=Source+Sans+3:wght@600;700&family=Montserrat:ital,wght@0,400;0,600;0,700;1,400&display=swap">
<style>
:root{
  --green:#0f9b4c;
  --green-dark:#0b7d3c;
  --navy:#1a1f2b;
  --black:#000;
  --ink:#111111;
  --card:#1b1b1b;
  --white:#ffffff;
  --muted:#d9d9d9;
}
*{box-sizing:border-box;margin:0;padding:0}
html,body{width:1200px;height:3871px;overflow:hidden;background:var(--black)}
body{font-family:"Montserrat",sans-serif;color:var(--white);position:relative}
.heading{font-family:"Source Sans 3",sans-serif;font-weight:700}
.accent{color:var(--green)}
section,header,footer{position:absolute;left:0;width:1200px}
.abs{position:absolute}
.btn{position:absolute;display:flex;align-items:center;justify-content:center;font-size:11px;font-weight:700;letter-spacing:.3px;text-transform:uppercase;border-radius:3px}
.btn-solid{background:var(--green);color:var(--white)}
.btn-dark{background:var(--ink);color:var(--white)}
.btn-outline{border:1.5px solid var(--green);color:var(--white)}
.btn-outline-white{border:1.5px solid var(--white);color:var(--white)}
.section-title{position:absolute;left:0;width:1200px;text-align:center;font-size:31px}
.underline{position:absolute;width:38px;height:4px;background:var(--green);left:581px}
.body-text{font-size:10.5px;line-height:20px;color:var(--muted);letter-spacing:-.1px}

/* header */
.site-header{top:0;height:62px;background:var(--navy)}
.brand{left:163px;top:17px;font-size:22px;letter-spacing:.2px}
.nav{left:512px;top:24px;display:flex;gap:25px;font-size:11px;font-weight:700}

/* hero */
.hero{top:62px;height:562px}
.hero-photo{position:absolute;inset:0;background:linear-gradient(180deg,#6b6a8f 0%,#b08aa0 28%,#c89c86 45%,#4c4b52 62%,#2c2c30 100%)}
.hero-title{left:163px;top:122px;font-size:67px;line-height:64px}
.hero-text{left:163px;top:275px;width:450px;font-size:11px;line-height:21px}
.dots{left:581px;top:531px;display:flex;gap:4px}
.dots span{width:6px;height:6px;border-radius:50%;background:#9a9a9a}
.dots span:first-child{background:var(--white)}

/* about */
.about{top:624px;height:504px;background:var(--black)}
.about-photo{left:163px;top:66px;width:490px;height:362px;border:4px solid var(--green);background:linear-gradient(180deg,#d88a2c 0%,#c4702a 40%,#8a7c6c 70%,#b9a993 100%)}
.about-box{left:585px;top:99px;width:452px;height:297px;background:var(--card);padding:30px 28px 30px 31px}
.about-box h2{font-size:31px;line-height:34px;margin-bottom:18px}
.about-box p{font-size:10.3px;line-height:20px;color:var(--muted);letter-spacing:-.15px}

/* services */
.services{top:1128px;height:532px;background:var(--ink)}
.service-card{position:absolute;top:130px;width:274px;text-align:center}
.service-photo{width:274px;height:187px}
.service-card h3{font-size:13.5px;font-weight:700;margin:18px 0 8px}

/* split */
.split{top:1660px;height:338px}
.split-half{position:absolute;top:0;width:600px;height:338px;text-align:center}
.shippers{left:0;background:linear-gradient(180deg,#3c3c3c,#2a2a2a)}
.carriers{left:600px;background:var(--green)}
.split-half h2{position:absolute;top:42px;width:600px;font-size:42px}
.split-half .bar{position:absolute;top:101px;left:281px;width:38px;height:4px;background:var(--white)}
.split-half p{position:absolute;top:120px;left:100px;width:400px;font-size:10.3px;line-height:20px;letter-spacing:-.15px;color:var(--white)}

/* why */
.why{top:1998px;height:608px;background:var(--ink)}
.why-item{position:absolute;width:220px}
.why-item h4{font-size:14.5px;font-weight:600;color:var(--green);margin-bottom:5px}
.why-item p{font-size:10.5px;line-height:19px;color:var(--white)}
.why-left{text-align:right}
.center-word{position:absolute;left:443px;width:300px;text-align:center;font-size:39px}

/* testimonials */
.testimonials{top:2606px;height:512px;background:var(--black)}
.quote-card{position:absolute;top:134px;width:238px;height:302px;background:var(--card);text-align:center;padding:0 15px}
.avatar{width:80px;height:80px;border-radius:50%;background:linear-gradient(180deg,#c9b7a3,#8a7462);margin:30px auto 22px}
.quote-card p{font-style:italic;font-size:10.2px;line-height:20.5px;letter-spacing:-.15px;color:var(--white);text-align:justify;text-align-last:center}
.quote-card .name{font-family:"Source Sans 3",sans-serif;font-weight:600;color:var(--green);font-size:15px;margin-top:12px}

/* contact */
.contact{top:3118px;height:436px;background:linear-gradient(180deg,#1aa259 0%,#0f9b4c 55%,#0c8a43 100%)}
.contact-row{position:absolute;left:243px;display:flex;gap:14px;font-size:11px;line-height:21px;align-items:flex-start}
.contact-row svg{flex:none;margin-top:2px}
.field{position:absolute;background:var(--white);color:#666;font-size:10px;padding:9px 8px}

/* footer */
.site-footer{top:3554px;height:317px;background:var(--black)}
.foot-logo{left:150px;top:75px;width:182px;text-align:center;font-size:35px;line-height:45px}
.socials{left:179px;top:166px;display:flex;gap:11px}
.socials span{width:23px;height:23px;border:1.5px solid var(--green);border-radius:50%}
.foot-col{position:absolute;top:60px;font-size:10.5px;line-height:22.5px}
.foot-col h5{font-size:11px;font-weight:700;margin-bottom:12px;letter-spacing:.3px}
.foot-contact{display:flex;gap:10px;line-height:16px;margin-bottom:8px;font-size:10px}
.foot-rule{left:133px;top:244px;width:934px;height:1px;background:#444}
.copyright{left:0;top:261px;width:1200px;text-align:center;font-size:10.5px}
</style>
</head>
<body>

<header class="site-header">
  <div class="abs brand heading">BRAVO FREIGHTWAY</div>
  <nav class="abs nav"><span>HOME</span><span>SHIPPERS</span><span>CARRIERS</span><span>ABOUT</span><span>CONTACT US</span></nav>
  <div class="btn btn-solid" style="left:900px;top:14px;width:137px;height:34px">Request a Quote</div>
</header>

<section class="hero">
  <div class="hero-photo" role="img" aria-label="Semi truck with trailer on a desert highway under a sunset sky"></div>
  <h1 class="abs hero-title heading">Welcome To<br>Bravo Freightway</h1>
  <p class="abs hero-text">Lorem ipsum dolor sit amet, consectetur adipiscing elit, sed do eiusmod tempor incididunt ut labore et dolore magna aliqua.</p>
  <div class="btn btn-solid" style="left:163px;top:334px;width:136px;height:34px">Get Started</div>
  <div class="abs dots"><span></span><span></span><span></span><span></span></div>
</section>

<section class="about">
  <div class="abs about-photo" role="img" aria-label="Truck parked in front of a sunlit mountain"></div>
  <div class="abs about-box">
    <h2 class="heading">About <span class="accent">Bravo Freightway</span></h2>
    <p>Lorem ipsum dolor sit amet, consectetur adipiscing elit, sed do eiusmod tempor incididunt ut labore et dolore magna aliqua. Quis ipsum suspendisse ultrices gravida. Risus commodo viverra maecenas accumsan lacus vel facilisis. perspiciatis unde omnis iste natus error sit voluptatem accusantium doloremque laudantium, totam rem aperiam, eaque ipsa quae ab illo inventore veritatis et quasi architecto beatae vitae dicta sunt explicabo.</p>
  </div>
  <div class="btn btn-solid" style="left:616px;top:324px;width:136px;height:34px">Learn More</div>
</section>

<section class="services">
  <h2 class="section-title heading" style="top:64px">Our <span class="accent">Services</span></h2>
  <div class="underline" style="top:106px"></div>
  <div class="service-card" style="left:163px">
    <div class="service-photo" role="img" aria-label="Forklift moving wrapped pallets in a warehouse" style="background:linear-gradient(180deg,#7d8a98,#c2552a 70%,#5a5a5a)"></div>
    <h3>LOREM IPSUM DOLOR SIT</h3>
    <p class="body-text" style="color:var(--white)">Lorem ipsum dolor sit amet, consectetur adipiscing elit, sed do eiusmod tempor incididunt ut labore et dolore magna aliqua.</p>
  </div>
  <div class="service-card" style="left:463px">
    <div class="service-photo" role="img" aria-label="Row of warehouse loading dock doors" style="background:linear-gradient(180deg,#9aa0a6,#5d6268 60%,#3b3f44)"></div>
    <h3>LOREM IPSUM DOLOR SIT</h3>
    <p class="body-text" style="color:var(--white)">Lorem ipsum dolor sit amet, consectetur adipiscing elit, sed do eiusmod tempor incididunt ut labore et dolore magna aliqua.</p>
  </div>
  <div class="service-card" style="left:762px">
    <div class="service-photo" role="img" aria-label="Two truck drivers standing in front of a red truck" style="background:linear-gradient(180deg,#7a3a3a,#4f5a6a 60%,#3a3f4a)"></div>
    <h3>LOREM IPSUM DOLOR SIT</h3>
    <p class="body-text" style="color:var(--white)">Lorem ipsum dolor sit amet, consectetur adipiscing elit, sed do eiusmod tempor incididunt ut labore et dolore magna aliqua.</p>
  </div>
  <div class="btn btn-outline" style="left:232px;top:429px;width:136px;height:34px">Learn More</div>
  <div class="btn btn-outline" style="left:532px;top:429px;width:136px;height:34px">Learn More</div>
  <div class="btn btn-outline" style="left:831px;top:429px;width:136px;height:34px">Learn More</div>
</section>

<section class="split">
  <div class="split-half shippers" role="img" aria-label="Warehouse loading docks in dark grey tones">
    <h2 class="heading">Shippers</h2>
    <div class="bar"></div>
    <p>Lorem ipsum dolor sit amet, consectetur adipiscing elit, sed do eiusmod tempor incididunt ut labore et dolore magna aliqua. Quis ipsum suspendisse ultrices gravida. Risus commodo viverra maecenas accumsan lacus vel facilisis. perspiciatis unde omnis iste natus error sit voluptatem accusantium doloremque laudantium, totam rem aperiam, eaque ipsa quae ab illo inventore veritatis et quasi architecto beatae vitae dicta sunt explicabo.</p>
    <div class="btn btn-solid" style="left:232px;top:251px;width:136px;height:34px">Learn More</div>
  </div>
  <div class="split-half carriers" role="img" aria-label="Truck front tinted in green">
    <h2 class="heading">Carriers</h2>
    <div class="bar"></div>
    <p>Lorem ipsum dolor sit amet, consectetur adipiscing elit, sed do eiusmod tempor incididunt ut labore et dolore magna aliqua. Quis ipsum suspendisse ultrices gravida. Risus commodo viverra maecenas accumsan lacus vel facilisis. perspiciatis unde omnis iste natus error sit voluptatem accusantium doloremque laudantium, totam rem aperiam, eaque ipsa quae ab illo inventore veritatis et quasi architecto beatae vitae dicta sunt explicabo.</p>
    <div class="btn btn-dark" style="left:232px;top:251px;width:136px;height:34px">Learn More</div>
  </div>
</section>

<section class="why">
  <h2 class="section-title heading" style="top:70px">Why <span class="accent">Choose Us ?</span></h2>
  <div class="underline" style="top:112px"></div>
  <svg class="abs" style="left:0;top:0" width="1200" height="608" viewBox="0 0 1200 608">
    <defs>
      <g id="truck-icon" fill="none" stroke="#fff" stroke-width="1.6" stroke-linecap="round" stroke-linejoin="round">
        <path d="M-10 -12 L-6 -12 L-2 8 L12 8"/>
        <rect x="-1" y="-9" width="10" height="7" transform="rotate(-12 4 -5)"/>
        <rect x="1" y="-1" width="9" height="6" transform="rotate(-12 5 2)"/>
        <circle cx="-1" cy="11" r="2.2"/>
        <circle cx="10" cy="11" r="2.2"/>
      </g>
    </defs>
    <path d="M452 197 A157 157 0 1 0 734 197" fill="none" stroke="#0f9b4c" stroke-width="3"/>
    <line x1="452" y1="197" x2="476" y2="153" stroke="#0f9b4c" stroke-width="2.5"/>
    <circle cx="476" cy="152" r="4" fill="#0f9b4c"/>
    <line x1="734" y1="197" x2="711" y2="153" stroke="#0f9b4c" stroke-width="2.5"/>
    <circle cx="711" cy="152" r="4" fill="#0f9b4c"/>
    <g fill="#0f9b4c" stroke="#fff" stroke-width="2">
      <circle cx="452" cy="197" r="27"/>
      <circle cx="457" cy="345" r="27"/>
      <circle cx="593" cy="424" r="27"/>
      <circle cx="729" cy="345" r="27"/>
      <circle cx="734" cy="197" r="27"/>
    </g>
    <use href="#truck-icon" x="452" y="197"/>
    <use href="#truck-icon" x="457" y="345"/>
    <use href="#truck-icon" x="593" y="424"/>
    <use href="#truck-icon" x="729" y="345"/>
    <use href="#truck-icon" x="734" y="197"/>
  </svg>
  <div class="center-word heading accent" style="top:222px">BRAVO</div>
  <div class="center-word heading" style="top:272px">FREIGHTWAY</div>
  <div class="why-item why-left" style="left:194px;top:164px"><h4>Lorem ipsum dolor</h4><p>Lorem ipsum dolor sit amet, consectetur adipiscing elit sed do.</p></div>
  <div class="why-item why-left" style="left:194px;top:304px"><h4>Lorem ipsum dolor</h4><p>Lorem ipsum dolor sit amet, consectetur adipiscing elit sed do.</p></div>
  <div class="why-item" style="left:785px;top:164px"><h4>Lorem ipsum dolor</h4><p>Lorem ipsum dolor sit amet, consectetur adipiscing elit sed do.</p></div>
  <div class="why-item" style="left:778px;top:304px"><h4>Lorem ipsum dolor</h4><p>Lorem ipsum dolor sit amet, consectetur adipiscing elit sed do.</p></div>
  <div class="why-item" style="left:483px;top:460px;text-align:center"><h4>Lorem ipsum dolor</h4><p>Lorem ipsum dolor sit amet, consectetur adipiscing elit sed do.</p></div>
</section>

<section class="testimonials">
  <h2 class="section-title heading" style="top:59px">Our <span class="accent">Client Testimonials</span></h2>
  <div class="underline" style="top:102px"></div>
  <div class="quote-card" style="left:207px">
    <div class="avatar" role="img" aria-label="Client portrait"></div>
    <p>Lorem ipsum dolor sit amet, consectetur adipiscing elit, sed do eiusmod tempor incididunt ut labore et dolore magna aliqua. Quis ipsum suspendisse ultrices gravida. Risus commodo viverra maecenas accumsan lacus vel facilisis.</p>
    <div class="name">- Dale Harper</div>
  </div>
  <div class="quote-card" style="left:481px">
    <div class="avatar" role="img" aria-label="Client portrait" style="background:linear-gradient(180deg,#8a9bb0,#5a7090)"></div>
    <p>Lorem ipsum dolor sit amet, consectetur adipiscing elit, sed do eiusmod tempor incididunt ut labore et dolore magna aliqua. Quis ipsum suspendisse ultrices gravida. Risus commodo viverra maecenas accumsan lacus vel facilisis.</p>
    <div class="name">- Dale Harper</div>
  </div>
  <div class="quote-card" style="left:756px">
    <div class="avatar" role="img" aria-label="Client portrait" style="background:linear-gradient(180deg,#a0b4c8,#4f6c8c)"></div>
    <p>Lorem ipsum dolor sit amet, consectetur adipiscing elit, sed do eiusmod tempor incididunt ut labore et dolore magna aliqua. Quis ipsum suspendisse ultrices gravida. Risus commodo viverra maecenas accumsan lacus vel facilisis.</p>
    <div class="name">- Dale Harper</div>
  </div>
</section>

<section class="contact" role="img" aria-label="Parked trucks tinted in green behind the contact form">
  <h2 class="section-title heading" style="top:56px;font-size:30px">Get In Touch</h2>
  <div class="underline" style="top:98px"></div>
  <div class="contact-row" style="top:182px">
    <svg width="20" height="22" viewBox="0 0 20 22"><path d="M10 1a7 7 0 0 0-7 7c0 5 7 13 7 13s7-8 7-13a7 7 0 0 0-7-7z" fill="#fff"/><circle cx="10" cy="8" r="2.6" fill="#0f9b4c"/></svg>
    <span style="width:215px">123 Lorem ipsum dolor sit amet, consectetur adipiscing.</span>
  </div>
  <div class="contact-row" style="top:236px">
    <svg width="20" height="20" viewBox="0 0 20 20"><path d="M4 1l4 4-2 3c1 3 3 5 6 6l3-2 4 4-3 3C8 19 1 12 1 4z" fill="#fff"/></svg>
    <span>+1 888 888 8888</span>
  </div>
  <div class="contact-row" style="top:282px">
    <svg width="20" height="16" viewBox="0 0 20 16"><rect x="1" y="2" width="18" height="13" fill="#fff"/><path d="M1 3l9 6 9-6" fill="none" stroke="#0f9b4c" stroke-width="1.6"/></svg>
    <span>hello@bravofreightway.example</span>
  </div>
  <div class="contact-row" style="top:327px">
    <svg width="20" height="20" viewBox="0 0 20 20" fill="none" stroke="#fff" stroke-width="1.6"><circle cx="10" cy="10" r="8.5"/><ellipse cx="10" cy="10" rx="3.5" ry="8.5"/><line x1="1.5" y1="10" x2="18.5" y2="10"/></svg>
    <span>www.bravofreightway.example</span>
  </div>
  <div class="field" style="left:556px;top:155px;width:197px;height:32px">First Name</div>
  <div class="field" style="left:758px;top:155px;width:197px;height:32px">Last Name</div>
  <div class="field" style="left:556px;top:199px;width:197px;height:32px">Email:</div>
  <div class="field" style="left:758px;top:199px;width:197px;height:32px">Phone:</div>
  <div class="field" style="left:556px;top:242px;width:399px;height:67px">Message:</div>
  <div class="btn btn-outline-white" style="left:556px;top:349px;width:136px;height:33px">Submit Now</div>
</section>

<footer class="site-footer">
  <div class="abs foot-logo heading">BRAVO<br>FREIGHTWAY</div>
  <div class="abs socials"><span></span><span></span><span></span><span></span></div>
  <div class="foot-col" style="left:372px"><h5>NAVIGATION</h5>Home<br>Shippers<br>Carriers<br>About<br>Contact Us</div>
  <div class="foot-col" style="left:497px"><h5>OUR SERVICES</h5>Lorem ipsum dolor<br>Sit amet consectetur<br>Adipiscing elit, sed do<br>Eiusmod tempor inci</div>
  <div class="foot-col" style="left:650px;width:200px">
    <h5>CONTACT US</h5>
    <div class="foot-contact"><svg width="10" height="13" viewBox="0 0 20 22"><path d="M10 1a7 7 0 0 0-7 7c0 5 7 13 7 13s7-8 7-13a7 7 0 0 0-7-7z" fill="#0f9b4c"/></svg><span>123 Lorem ipsum dolor sit amet, consectetur</span></div>
    <div class="foot-contact"><svg width="11" height="11" viewBox="0 0 20 20"><path d="M4 1l4 4-2 3c1 3 3 5 6 6l3-2 4 4-3 3C8 19 1 12 1 4z" fill="#0f9b4c"/></svg><span>Call Us:<br>+1 888 888 8888</span></div>
    <div class="foot-contact"><svg width="11" height="9" viewBox="0 0 20 16"><rect x="1" y="2" width="18" height="13" fill="#0f9b4c"/></svg><span>Email Address:<br>hello@bravofreightway.example</span></div>
  </div>
  <div class="foot-col" style="left:865px"><h5>SIGN UP EMAIL</h5>Sign up for our email list</div>
  <div class="field" style="left:866px;top:122px;width:164px;height:29px;border-radius:3px;font-size:9.5px;padding:8px 14px">Email address</div>
  <div class="btn btn-solid" style="left:866px;top:162px;width:164px;height:30px;font-size:9.5px">Subscribe Now</div>
  <div class="abs foot-rule"></div>
  <div class="abs copyright">© copyrights 2022 <span class="accent">BRAVO FREIGHTWAY</span> &nbsp;|&nbsp;&nbsp;&nbsp; All rights reserved.</div>
</footer>

</body>
</html>
```